Veradine Contracting Folder

Creating a design for the cover of our folders that we pass to our customers

Want to keep the same look as our colors and fonts as attached

```html
<!DOCTYPE html>
<html lang="en">
<head>
<meta charset="utf-8">
<title>Veradine Contracting Folder</title>
<link rel="stylesheet" href="https://fonts.googleapis.com/css2?family=Questrial&display=swap">
<style>
  :root {
    --stage: #d8d8da;
    --cover-top: #b9b8bb;
    --cover-bottom: #a8a7aa;
    --skyline: #a3a2a6;
    --brand-blue: #2f3a96;
    --brand-blue-light: #3e4aa6;
    --brand-gold: #e2c341;
    --ink-white: #f4f4f6;
    --photo-light: #d6d6d6;
    --photo-dark: #5e5e5e;
  }
  * { margin: 0; padding: 0; box-sizing: border-box; }
  html, body {
    width: 1200px;
    height: 1200px;
    overflow: hidden;
    background: var(--stage);
    font-family: "Questrial", "Century Gothic", sans-serif;
  }
  .folder-cover {
    position: absolute;
    left: 190px;
    top: 62px;
    width: 820px;
    height: 1077px;
    background: linear-gradient(180deg, var(--cover-top), var(--cover-bottom));
    border-radius: 0 22px 22px 0;
    overflow: hidden;
  }
  .skyline {
    position: absolute;
    left: 0;
    top: 60px;
    width: 100%;
    height: 216px;
    background: linear-gradient(180deg, rgba(163,162,166,0) 0%, var(--skyline) 70%, rgba(163,162,166,0.6) 100%);
  }
  .brand-name {
    position: absolute;
    left: 0;
    top: 92px;
    width: 100%;
    text-align: center;
    color: var(--brand-blue);
    font-size: 56px;
    font-weight: 400;
    line-height: 1.2;
  }
  .service-band {
    position: absolute;
    left: 0;
    top: 268px;
    width: 100%;
    height: 72px;
    background: var(--brand-blue);
    border-bottom: 7px solid var(--brand-gold);
  }
  .service-band::before {
    content: "";
    position: absolute;
    left: 0; top: 0;
    width: 100%;
    height: 18px;
    background: var(--brand-blue-light);
  }
  .service-title {
    position: relative;
    padding-top: 20px;
    text-align: center;
    color: var(--ink-white);
    font-size: 38px;
    font-weight: 400;
    letter-spacing: 1px;
  }
  .photo-row {
    position: absolute;
    left: 0;
    top: 340px;
    width: 100%;
    height: 318px;
    display: flex;
  }
  .photo { height: 100%; }
  .photo-handshake-house {
    width: 410px;
    background: linear-gradient(160deg, var(--photo-light) 0%, #a8a8a8 55%, #7a7a7a 100%);
  }
  .photo-office-meeting {
    width: 410px;
    background: linear-gradient(200deg, #e6e6e6 0%, #9a9a9a 50%, var(--photo-dark) 100%);
    border-left: 1px solid #ddd;
  }
  .website {
    position: absolute;
    left: 0;
    top: 672px;
    width: 100%;
    text-align: center;
    color: var(--brand-blue);
    font-size: 17px;
    letter-spacing: 3px;
  }
  .address {
    position: absolute;
    left: 0;
    top: 972px;
    width: 100%;
    text-align: center;
    color: var(--ink-white);
    font-size: 29px;
    line-height: 41px;
    font-style: normal;
  }
</style>
</head>
<body>
  <main class="folder-cover">
    <div class="skyline" role="img" aria-label="Faint city skyline silhouette"></div>

    <header class="brand">
      <div class="brand-name">Veradine Contracting</div>
    </header>

    <section class="service-band">
      <h1 class="service-title">Painting &amp; Contracting</h1>
    </section>

    <section class="photo-row">
      <div class="photo photo-handshake-house" role="img" aria-label="Black and white photo of a handshake in front of a suburban house"></div>
      <div class="photo photo-office-meeting" role="img" aria-label="Black and white photo of business people shaking hands in an office"></div>
    </section>

    <p class="website">www.veradinecontracting.com</p>

    <address class="address">
      Dummy city<br>
      Dummy Country Land
    </address>
  </main>
</body>
</html>
```